Business Card Design

A business card design must match as a cleaning company.
We do house cleaning, office, cafe , function center , club and so on.

Industry/Entity Type

House

Contact Information for Business Card

Bright Lane cleaning services
Mara Delvin
Director
0428395146
1300 917 254
Brightlane.cleaning@bluvex.com

```html
<!DOCTYPE html>
<html lang="en">
<head>
<meta charset="utf-8">
<title>Bright Lane cleaning services – Business Card</title>
<link rel="stylesheet" href="https://fonts.googleapis.com/css2?family=Source+Sans+3:wght@400;600&display=swap">
<style>
  :root {
    --backdrop: #2b2e31;
    --wood-dark: #2a1a0e;
    --wood-mid: #7a4a1c;
    --wood-warm: #b57a34;
    --wood-light: #c89a5c;
    --band-fill: rgba(150, 138, 126, 0.55);
    --panel-fill: rgba(118, 108, 100, 0.85);
    --side-block: #6e645c;
    --accent-orange: #f2a21c;
    --text-light: #d9d6d2;
    --text-soft: #c4c0bb;
  }
  * { margin: 0; padding: 0; box-sizing: border-box; }
  html, body {
    width: 1200px; height: 900px; overflow: hidden;
    background: var(--backdrop);
    font-family: "Source Sans 3", "Myriad Pro", sans-serif;
  }
  .business-card {
    position: absolute; left: 100px; top: 160px;
    width: 1000px; height: 580px;
    overflow: hidden;
    box-shadow: 0 20px 50px rgba(0,0,0,0.5);
  }
  .card-photo {
    position: absolute; inset: 0;
    background:
      radial-gradient(ellipse at 78% 22%, rgba(232,214,80,0.35) 0 10%, transparent 24%),
      radial-gradient(ellipse at 80% 48%, rgba(220,120,160,0.35) 0 10%, transparent 22%),
      radial-gradient(ellipse at 30% 18%, var(--wood-warm) 0%, transparent 45%),
      linear-gradient(100deg, var(--wood-dark) 0%, var(--wood-mid) 30%, var(--wood-mid) 48%, var(--wood-light) 62%, var(--wood-warm) 80%, var(--wood-dark) 100%);
  }
  .side-block {
    position: absolute; left: 835px; top: 120px;
    width: 140px; height: 180px;
    background: var(--side-block);
  }
  .company-band {
    position: absolute; left: 0; top: 220px;
    width: 660px; height: 72px;
    background: var(--band-fill);
    display: flex; align-items: center;
    padding-left: 40px;
  }
  .company-name {
    color: var(--accent-orange);
    font-size: 44px; font-weight: 400;
    white-space: nowrap;
  }
  .contact-panel {
    position: absolute; left: 60px; top: 322px;
    width: 720px; height: 258px;
    background: var(--panel-fill);
    padding: 22px 40px;
  }
  .person-name {
    color: var(--text-light);
    font-size: 60px; font-weight: 600; line-height: 1;
  }
  .person-role {
    color: var(--text-light);
    font-size: 48px; font-weight: 600; line-height: 1.1;
    margin-bottom: 18px;
  }
  .contact-line {
    color: var(--text-soft);
    font-size: 32px; font-weight: 400; line-height: 1.25;
    white-space: nowrap;
  }
</style>
</head>
<body>
  <div class="business-card">
    <div class="card-photo" role="img" aria-label="Photo of a yellow-gloved hand wiping a wooden floor with a pink cloth"></div>
    <div class="side-block"></div>
    <div class="company-band">
      <h1 class="company-name">Bright Lane cleaning services</h1>
    </div>
    <div class="contact-panel">
      <p class="person-name">Mara Delvin</p>
      <p class="person-role">Director</p>
      <p class="contact-line">Contact: 0428395146, 1300 917 254</p>
      <p class="contact-line">E-mail: Brightlane.cleaning@bluvex.com</p>
    </div>
  </div>
</body>
</html>
```